2022 Landscaping Services

Please use the prior year design as an example. Similar style but DO NOT COPY IT EXACTLY- you can use different photos from our website if you like. Same text for year 2022.
Design should clearly depict the differences between the 3 products so people can buy one of them. Be creative!

size 8.5" x 11"

Must provide source file in photoshop if you are winner

Requirements
Must have
• Same text as original flier but with year 2022

```html
<!DOCTYPE html>
<html lang="en">
<head>
<meta charset="utf-8">
<title>2022 Gravesite Landscaping Package</title>
<link href="https://fonts.googleapis.com/css2?family=Montserrat:wght@400;500;600;700&family=Lobster&display=swap" rel="stylesheet">
<style>
:root{
  --maroon:#6e0f1c;
  --maroon-deep:#4d0711;
  --stone:#cdc8c6;
  --paper:#eae8e8;
  --white:#ffffff;
  --ink:#2b2230;
  --bg:#9ea0a8;
  --rule-soft:#b98a90;
}
*{box-sizing:border-box;margin:0;padding:0}
html,body{width:1200px;height:900px;overflow:hidden}
body{background:var(--bg);font-family:"Montserrat",sans-serif;display:flex;align-items:center;justify-content:center}
.flyer{position:relative;width:660px;height:854px;background:var(--paper);overflow:hidden;box-shadow:0 6px 24px rgba(0,0,0,.25)}
.hero-photo{position:absolute;left:0;top:0;width:660px;height:310px;
  background:radial-gradient(circle at 78% 18%,#fff4c8 0,#e9c46a 12%,rgba(200,150,60,0) 35%),
  linear-gradient(180deg,#9c7a2e 0%,#7d6a3a 40%,#8e9290 62%,#6f8a3c 80%,#4f6a2a 100%)}
.brand{position:absolute;left:18px;top:26px;background:var(--white);padding:8px 14px;display:flex;align-items:center;gap:8px}
.brand-dot{width:12px;height:12px;border-radius:50%;background:var(--maroon)}
.brand-name{font-size:13px;font-weight:500;color:var(--maroon);letter-spacing:.5px}
.band{position:absolute;left:0;top:0}
.title{position:absolute;right:30px;top:205px;text-align:right;color:var(--white);font-weight:600;line-height:1}
.title .year{font-size:46px;display:block}
.title .line{font-size:29px;display:block;margin-top:8px}

.services{position:absolute;left:20px;top:422px;width:196px;height:372px;background:var(--white);padding:14px 14px 0 20px}
.services h2{font-size:19px;line-height:1;font-weight:700;color:var(--maroon)}
.service-list{position:absolute;left:20px;top:68px;list-style:none}
.service-list li{height:34px;font-size:9.5px;font-weight:600;color:var(--ink);line-height:1.2;display:flex;align-items:center}
.valid{position:absolute;left:20px;bottom:16px;font-size:14px;font-weight:700;color:var(--ink);line-height:1.15}

.plan{position:absolute;text-align:center}
.plan-head{display:flex;flex-direction:column;justify-content:center;color:var(--ink)}
.plan-head .name{font-size:13px;font-weight:700}
.plan-head .kind{font-size:9.5px;font-weight:600}
.plan-desc{font-size:8px;line-height:1.3;padding:8px 6px 0}
.seasonal{left:216px;top:390px;width:140px;height:420px;background:var(--maroon)}
.seasonal .plan-head{height:44px;background:var(--stone)}
.perpetual{left:356px;top:352px;width:148px;height:466px;background:#dedad9;box-shadow:0 4px 12px rgba(0,0,0,.3);z-index:2}
.perpetual .plan-head{height:66px;background:var(--maroon);color:var(--white)}
.perpetual .plan-head .name{font-size:14px;font-weight:600}
.perpetual .plan-desc{color:var(--ink)}
.basic{left:504px;top:340px;width:136px;height:472px;background:var(--maroon-deep)}
.basic .plan-head{height:44px;background:var(--stone)}
.seasonal .plan-desc,.basic .plan-desc{color:#f1dede}
.badge{position:absolute;left:128px;top:-14px;width:38px;height:38px;border-radius:50%;background:var(--white);border:2px solid var(--maroon);display:flex;align-items:center;justify-content:center;font-family:"Lobster",cursive;font-size:9px;line-height:.95;color:var(--maroon);z-index:3}

.marks{position:absolute;left:0;width:100%;list-style:none}
.marks li{height:34px;display:flex;align-items:center;justify-content:center}
.mark{width:16px;height:16px}
.seasonal .mark,.basic .mark{color:#f3dcdc}
.perpetual .mark{color:var(--maroon)}

.price-rule{position:absolute;left:12px;right:12px;height:2px}
.seasonal .price-rule,.basic .price-rule{background:var(--rule-soft)}
.perpetual .price-rule{background:var(--maroon);height:3px}
.prices{position:absolute;left:0;width:100%;display:flex;justify-content:center}
.price{padding:0 5px;color:var(--white)}
.price + .price{border-left:1px solid var(--rule-soft)}
.price strong{display:block;font-size:15px;font-weight:600}
.price span{font-size:7px}
.big-price{font-size:24px;font-weight:600;line-height:1.2}
.perpetual .big-price{color:var(--maroon)}
.basic .big-price{color:var(--white)}
.price-note{position:absolute;left:0;width:100%;font-size:8px;line-height:1.3;padding:0 14px}
.seasonal .price-note,.basic .price-note{color:#e9cdd0}
.perpetual .price-note{color:var(--ink)}

.footer-rule{position:absolute;left:240px;right:20px;top:818px;height:2px;background:var(--maroon)}
.address{position:absolute;left:0;top:824px;width:260px;height:30px;background:var(--maroon);color:var(--white);font-size:11px;font-weight:600;display:flex;align-items:center;justify-content:center}
.contact{position:absolute;right:22px;top:830px;font-size:12px;font-weight:600;color:var(--maroon)}
.contact .sep{margin:0 8px}
</style>
</head>
<body>
<svg width="0" height="0" style="position:absolute">
  <defs>
    <symbol id="tick" viewBox="0 0 16 16"><circle cx="8" cy="8" r="6.6" fill="none" stroke="currentColor" stroke-width="1.4"/><path d="M5 8.2l2 2 4-4.2" fill="none" stroke="currentColor" stroke-width="1.6" stroke-linecap="round" stroke-linejoin="round"/></symbol>
    <symbol id="cross" viewBox="0 0 16 16"><circle cx="8" cy="8" r="6.6" fill="none" stroke="currentColor" stroke-width="1.4"/><path d="M5.6 5.6l4.8 4.8M10.4 5.6l-4.8 4.8" fill="none" stroke="currentColor" stroke-width="1.6" stroke-linecap="round"/></symbol>
  </defs>
</svg>

<main class="flyer">
  <div class="hero-photo" role="img" aria-label="Photo of a cemetery path lined with headstones and autumn trees at sunset"></div>

  <div class="brand"><span class="brand-dot"></span><span class="brand-name">BROOKHAVEN CEMETERY</span></div>

  <svg class="band" width="660" height="440" viewBox="0 0 660 440">
    <defs><linearGradient id="bandFill" x1="0" y1="0" x2="1" y2="0"><stop offset="0" stop-color="#7d1827"/><stop offset="1" stop-color="#5a0a15"/></linearGradient></defs>
    <polygon points="0,300 660,190 660,440 0,440" fill="url(#bandFill)"/>
  </svg>

  <h1 class="title"><span class="year">2022</span><span class="line">GRAVESITE</span><span class="line">LANDSCAPING PACKAGE</span></h1>

  <section class="services">
    <h2>SERVICES<br>OFFERED</h2>
    <ul class="service-list">
      <li>WEDDING &amp; TRIMMING ON<br>YOUR GRAVESITE</li>
      <li>PAYMENT ENSURED<br>FOREVER GRAVE CAR</li>
      <li>WEDDING &amp; TRIMMING ON<br>YOUR GRAVESITE</li>
      <li>PAYMENT ENSURED<br>FOREVER GRAVE CAR</li>
      <li>PAYMENT ENSURED<br>FOREVER GRAVE CAR</li>
      <li>WEDDING &amp; TRIMMING ON<br>YOUR GRAVESITE</li>
      <li>PAYMENT ENSURED<br>FOREVER GRAVE CAR</li>
    </ul>
    <p class="valid">Valid through<br>10/31/22</p>
  </section>

  <section class="plan seasonal">
    <div class="plan-head"><span class="name">SEASONAL</span><span class="kind">CARE ENDOWMENT</span></div>
    <p class="plan-desc">Approximately every 7 weeks during the growing season:<br>Mid-April through Mid-October</p>
    <ul class="marks" style="top:100px">
      <li><svg class="mark"><use href="#cross"/></svg></li>
      <li><svg class="mark"><use href="#cross"/></svg></li>
      <li><svg class="mark"><use href="#cross"/></svg></li>
      <li><svg class="mark"><use href="#cross"/></svg></li>
      <li><svg class="mark"><use href="#cross"/></svg></li>
      <li><svg class="mark"><use href="#cross"/></svg></li>
      <li><svg class="mark"><use href="#cross"/></svg></li>
    </ul>
    <div class="price-rule" style="top:346px"></div>
    <div class="prices" style="top:352px">
      <div class="price"><strong>$357</strong><span>3 Years</span></div>
      <div class="price"><strong>$238</strong><span>2 Years</span></div>
      <div class="price"><strong>$119</strong><span>1 Years</span></div>
    </div>
    <p class="price-note" style="top:386px">Multi-year payment locks<br>in current rates</p>
  </section>

  <section class="plan perpetual">
    <div class="badge">Most<br>Popular</div>
    <div class="plan-head"><span class="name">PERPETUAL</span><span class="kind">CARE ENDOWMENT</span></div>
    <p class="plan-desc">Approximately every 7 weeks during the growing season:<br>Mid-April through Mid-October</p>
    <ul class="marks" style="top:138px">
      <li><svg class="mark"><use href="#tick"/></svg></li>
      <li><svg class="mark"><use href="#tick"/></svg></li>
      <li><svg class="mark"><use href="#tick"/></svg></li>
      <li><svg class="mark"><use href="#tick"/></svg></li>
      <li><svg class="mark"><use href="#tick"/></svg></li>
      <li><svg class="mark"><use href="#tick"/></svg></li>
      <li><svg class="mark"><use href="#tick"/></svg></li>
    </ul>
    <div class="price-rule" style="top:384px"></div>
    <div class="prices" style="top:390px"><span class="big-price">$313</span></div>
    <p class="price-note" style="top:422px">12 Monthly payments.<br>Call for single payment<br>discount.</p>
  </section>

  <section class="plan basic">
    <div class="plan-head"><span class="name">BASIC</span><span class="kind">CARE ENDOWMENT</span></div>
    <p class="plan-desc">2 times per year:<br>Mid-May &amp; Mid-September</p>
    <ul class="marks" style="top:150px">
      <li><svg class="mark"><use href="#tick"/></svg></li>
      <li><svg class="mark"><use href="#tick"/></svg></li>
      <li><svg class="mark"><use href="#cross"/></svg></li>
      <li><svg class="mark"><use href="#cross"/></svg></li>
      <li><svg class="mark"><use href="#cross"/></svg></li>
      <li><svg class="mark"><use href="#cross"/></svg></li>
      <li><svg class="mark"><use href="#cross"/></svg></li>
    </ul>
    <div class="price-rule" style="top:396px"></div>
    <div class="prices" style="top:402px"><span class="big-price">$255</span></div>
    <p class="price-note" style="top:434px">12 Monthly payments.<br>Call for single payment<br>discount.</p>
  </section>

  <div class="footer-rule"></div>
  <p class="address">48 Elm Ave. Fairview NJ 07099</p>
  <p class="contact">(555) 214-0388<span class="sep">|</span>brookhavencemetery.org</p>
</main>
</body>
</html>
```